Engineering Consultant Business Card

I'm starting a new business as a high-end engineering consultant in a niche field. I've attached the jpg for my logo plus the branding guideline document that I've been following. You can see my business website here: www.tarvikworks.com
I'd like a business card that has the logo on one side, then the other side has (in any order): Tarvik Works, Inc.
Dana Whitlock
President and Chief EMC Engineer
www.tarvikworks.com
dana@tarvikworks.com
Optional: motto "We will solve your EMC problems as early as possible—ideally before they even start."
I'm not planning on including a phone number
Target Market(s)
Businesses, especially makers of electronics hardware
Industry/Entity Type
Electrical engineering
Contact Information for Business Card
Company name, my name, website, email

```html
<!DOCTYPE html>
<html lang="en">
<head>
<meta charset="utf-8">
<title>Tarvik Works, Inc. — Business Card</title>
<link rel="stylesheet" href="https://fonts.googleapis.com/css2?family=Poppins:wght@500;600;700&family=Old+Standard+TT&display=swap">
<style>
  :root {
    --stage: #e7e8ec;
    --navy: #2f3f95;
    --navy-mid: #3450a8;
    --blue-end: #3f7dbb;
    --white: #ffffff;
    --ink: #0d0f1a;
    --link-violet: #6a4cf0;
    --card-shadow: 0 14px 34px rgba(20, 30, 70, 0.28);
  }
  * { box-sizing: border-box; margin: 0; padding: 0; }
  html, body { width: 1200px; height: 911px; overflow: hidden; background: var(--stage); }
  .sheet {
    width: 1200px; height: 911px;
    display: flex; align-items: center; justify-content: center; gap: 40px;
  }
  .card {
    position: relative; width: 540px; height: 309px; overflow: hidden;
    background: linear-gradient(135deg, var(--navy) 0%, var(--navy-mid) 40%, var(--blue-end) 100%);
    box-shadow: var(--card-shadow);
    font-family: "Poppins", sans-serif;
  }
  .brand-mark {
    position: absolute; color: var(--white); font-weight: 600;
    letter-spacing: 0.5px; white-space: nowrap;
  }
  /* logo side */
  .card--logo .brand-mark { left: 0; right: 0; top: 112px; text-align: center; font-size: 40px; }
  .card--logo .web-band {
    position: absolute; left: 0; right: 0; bottom: 0; height: 34px;
    background: var(--white); display: flex; align-items: center; padding-left: 28px;
  }
  .web-band .website {
    font-family: "Old Standard TT", serif; font-size: 17px; color: var(--link-violet);
  }
  /* details side */
  .card--details .panel { position: absolute; inset: 0; }
  .card--details .brand-mark { left: 38px; top: 120px; font-size: 27px; }
  .company {
    position: absolute; left: 318px; top: 34px;
    font-family: "Old Standard TT", serif; font-size: 21px; line-height: 1.05; color: var(--ink);
  }
  .person { position: absolute; left: 318px; top: 128px; }
  .person .name { font-weight: 700; font-size: 25px; color: var(--white); line-height: 1.1; }
  .person .role { font-weight: 600; font-size: 10.5px; color: var(--ink); margin-top: 2px; }
  .email {
    position: absolute; right: 26px; bottom: 18px;
    font-weight: 500; font-size: 11px; color: var(--white);
  }
</style>
</head>
<body>
<main class="sheet">
  <section class="card card--logo" aria-label="Card front">
    <div class="brand-mark">Tarvik Works</div>
    <div class="web-band"><span class="website">www.tarvikworks.com</span></div>
  </section>

  <section class="card card--details" aria-label="Card back">
    <svg class="panel" viewBox="0 0 540 309" width="540" height="309" aria-hidden="true">
      <path d="M0 0 H262 C318 0 322 66 306 128 C286 206 214 272 132 309 H0 Z" fill="#3550ab"/>
      <path d="M0 0 H246 C300 0 304 62 290 122 C270 200 200 268 120 309 H0 Z" fill="var(--navy)"/>
      <path d="M196 309 C226 280 246 262 274 262 C300 262 312 284 324 309 Z" fill="#2f43a0"/>
    </svg>
    <div class="brand-mark">Tarvik Works</div>
    <div class="company">Tarvik<br>Works, Inc.</div>
    <div class="person">
      <div class="name">Dana Whitlock</div>
      <div class="role">Chief EMC Engineer</div>
    </div>
    <div class="email">dana@tarvikworks.com</div>
  </section>
</main>
</body>
</html>
```